Logistics and freight company requires website

Hi, a logistic and freight company which is based in the United States needs an industry standard website for its activities. We are into forwarding and courier goods from within United States and Canada. We deliver a wide range of goods from shipping of electronics to document, clothings, etc. The proposed website should be comtemporary and youthful. I require brilliant colors for the website. The website should be the basic things of a site. There should a category for shipping electronics, clothings, documents and others( stuffs not listed within the three I mentioned).

```html
<!DOCTYPE html>
<html lang="en">
<head>
<meta charset="utf-8">
<title>SwiftCargo – Transport &amp; Logistics Services</title>
<link href="https://fonts.googleapis.com/css2?family=Open+Sans:wght@600;700&family=Roboto:ital,wght@0,300;0,400;0,500;0,700;1,400&display=swap" rel="stylesheet">
<style>
:root{
  --teal:#22b5a8;
  --cyan-btn:#0fa6e8;
  --blue:#1b7fd2;
  --ink:#333;
  --cream:#fdf7ea;
  --orange:#f5a000;
  --footer:#2b2b2b;
  --footer-text:#cfcfcf;
  --brand-blue:#1d5fa8;
  --block:#f3f3f3;
  --white:#fff;
}
*{box-sizing:border-box;margin:0;padding:0}
html,body{width:1200px;height:2817px;overflow:hidden}
body{position:relative;font-family:"Roboto",Arial,sans-serif;color:var(--ink);background:var(--white)}
.abs{position:absolute}
a{color:inherit;text-decoration:none}

/* top bar */
.topbar{left:0;top:0;width:1200px;height:28px;background:var(--teal);color:var(--white);font-size:12px}
.topbar .phone{left:94px;top:5px;font-size:15px;display:flex;align-items:center;gap:6px}
.social{display:flex;gap:4px}
.social span{width:20px;height:20px;display:block;background:var(--brand-blue)}
.topbar .social{left:220px;top:4px}
.topbar .social span{border:1px solid rgba(255,255,255,.6)}
.toplinks{top:8px;font-size:11px;font-weight:500;letter-spacing:.2px}
.toplinks a{position:absolute;white-space:nowrap}

/* header */
.header{left:0;top:28px;width:1200px;height:76px;background:var(--white)}
.brand{display:flex;align-items:center;gap:8px;font-size:27px;font-weight:400;color:var(--brand-blue);letter-spacing:-.3px}
.brand .dot{width:14px;height:14px;background:var(--teal);border-radius:50%}
.header .brand{left:94px;top:20px}
.nav a{position:absolute;top:31px;font-size:13px;font-weight:700;color:#333}
.nav a.active::after{content:"";position:absolute;left:0;right:0;bottom:-9px;height:3px;background:var(--teal)}
.search{left:933px;top:24px;width:26px;height:26px;border-radius:50%;background:#bbb}
.btn-quote{display:flex;align-items:center;justify-content:center;background:var(--cyan-btn);color:var(--white);font-size:13px;font-weight:700;border-radius:2px}
.header .btn-quote{left:986px;top:15px;width:120px;height:47px}

/* hero */
.hero{left:0;top:104px;width:1200px;height:536px;background:linear-gradient(180deg,#5d8fc4 0%,#9cbfe0 38%,#a9c3d8 55%,#2e5b8d 70%,#1d3d66 100%)}
.hero-title{left:0;top:84px;width:1200px;text-align:center;font-family:"Open Sans",Arial,sans-serif;font-weight:700;font-size:55px;line-height:56px;color:var(--white);text-shadow:0 2px 6px rgba(0,0,0,.25)}
.arrow-box{top:183px;width:42px;height:83px;background:rgba(40,40,40,.75);display:flex;align-items:center;justify-content:center}
.dots{left:579px;top:429px;display:flex;gap:3px}
.dots span{width:8px;height:8px;border-radius:50%;border:1px solid var(--white)}
.dots span.on{background:var(--white)}
.quote-bar{left:0;top:452px;width:1200px;height:84px;background:linear-gradient(180deg,rgba(15,35,70,0) 0%,rgba(15,35,70,.55) 100%)}
.quote-label{left:274px;top:588px;color:var(--white);font-size:17px}
.q-input{top:578px;height:40px;background:var(--white);font-size:13px;color:#888;padding:12px 10px}
.q-go{left:774px;top:578px;width:49px;height:40px;background:var(--teal);color:var(--white);font-size:15px;display:flex;align-items:center;justify-content:center}

/* section headings */
.h2{font-size:31px;font-weight:300;color:#333}
.h2::after{content:"";display:block;width:72px;height:2px;background:var(--teal);margin-top:8px}
.para{font-size:14px;line-height:22px;color:#444}

/* why / how */
.feature{display:flex;align-items:center;gap:22px;font-size:17px;font-weight:500;color:#333}
.feature .ic{width:52px;height:52px;border-radius:50%;border:2px solid var(--teal);display:flex;align-items:center;justify-content:center}
.dash{left:92px;width:468px;border-top:1px dashed #999}
.video{left:612px;top:870px;width:494px;height:230px;background:linear-gradient(180deg,#d7d8dc 0%,#c8b79b 55%,#b58a52 100%)}

/* deliver */
.deliver-photo{left:0;top:1180px;width:586px;height:465px;background:linear-gradient(180deg,#6f9fd2 0%,#a8c4df 45%,#8a8578 62%,#3f3d3b 100%)}
.deliver{left:586px;top:1180px;width:614px;height:465px;background:linear-gradient(135deg,#1f86d8,#1670c2)}
.cat{display:flex;align-items:center;gap:10px;color:var(--white);font-size:17px;font-weight:500}
.cat .ic{width:55px;height:55px;border-radius:50%;border:2px solid rgba(255,255,255,.85);display:flex;align-items:center;justify-content:center}
.btn-view{left:639px;top:1510px;width:120px;height:47px;background:var(--teal);color:var(--white);font-size:14px;font-weight:700;display:flex;align-items:center;justify-content:center;border-radius:2px}

/* locations / testimonial */
.cream{left:0;top:1645px;width:1200px;height:481px;background:var(--cream)}
.map-card{top:1865px;width:242px;height:184px;background:var(--white);border:1px solid #e4e0d6}
.map-card .label{position:absolute;top:10px;width:100%;text-align:center;font-size:17px;color:#1d6fc4}
.map-shape{position:absolute;left:30px;top:40px;width:182px;height:128px;border-radius:18px}
.quote-text{left:699px;top:1798px;width:407px;font-size:14px;font-style:italic;line-height:25px;color:#444}
.client-name{left:699px;top:1960px;font-size:14px;font-weight:700;color:#333}
.client-co{left:699px;top:1980px;font-size:14px;color:#444}
.nav-btn{top:2006px;width:39px;height:36px;background:var(--orange);display:flex;align-items:center;justify-content:center}

/* clients */
.clients-h{left:0;top:2176px;width:1200px;text-align:center}
.clients-h .h2{display:inline-block}
.clients-h .h2::after{margin:8px auto 0}
.client-box{top:2246px;width:151px;height:116px;background:var(--block)}

/* footer */
.footer{left:0;top:2432px;width:1200px;height:385px;background:var(--footer)}
.f-h{top:2505px;font-size:16px;font-weight:500;color:var(--teal)}
.f-text{top:2540px;font-size:12px;line-height:22px;color:var(--footer-text)}
.f-list{top:2540px;font-size:12px;line-height:21.6px;list-style:none;color:var(--footer-text)}
.f-contact{font-size:12px;line-height:22px;display:flex;gap:8px;color:var(--footer-text)}
.footer-rule{left:92px;top:2710px;width:1014px;border-top:1px solid #444}
.copy{left:485px;top:2766px;font-size:12px;color:var(--footer-text)}
</style>
</head>
<body>

<div class="abs topbar">
  <div class="abs phone">
    <svg width="13" height="13" viewBox="0 0 24 24"><path fill="#fff" d="M6.6 10.8a15 15 0 0 0 6.6 6.6l2.2-2.2c.3-.3.7-.4 1-.2 1.1.4 2.3.6 3.6.6.6 0 1 .4 1 1V20c0 .6-.4 1-1 1A17 17 0 0 1 3 4c0-.6.4-1 1-1h3.5c.6 0 1 .4 1 1 0 1.3.2 2.5.6 3.6.1.3 0 .7-.2 1z"/></svg>
    0155 010 2040
  </div>
  <div class="abs social"><span></span><span></span><span></span><span></span></div>
  <div class="abs toplinks" style="left:0;width:1200px">
    <a style="left:745px">HELP</a>
    <a style="left:807px">SUPPORT</a>
    <a style="left:893px">MY BOOKINGS</a>
    <a style="left:1003px">BECOME A MEMBER</a>
  </div>
</div>

<header class="abs header">
  <div class="abs brand"><span class="dot"></span>SwiftCargo</div>
  <nav class="nav">
    <a class="active" style="left:368px">HOME</a>
    <a style="left:445px">ABOUT US</a>
    <a style="left:550px">SERVICES</a>
    <a style="left:650px">LOCATIONS</a>
    <a style="left:762px">NEWS</a>
    <a style="left:840px">CONTACT</a>
  </nav>
  <div class="abs search"></div>
  <a class="abs btn-quote">QUICK QUOTE</a>
</header>

<section class="abs hero" role="img" aria-label="Photo of a large container ship loaded with colourful cargo containers at sea under a blue sky">
  <h1 class="abs hero-title">TRANSPORT &amp;<br>LOGISTICS SERVICES</h1>
  <div class="abs arrow-box" style="left:0"><svg width="14" height="26" viewBox="0 0 14 26"><path d="M12 2 2 13l10 11" stroke="#fff" stroke-width="2" fill="none"/></svg></div>
  <div class="abs arrow-box" style="left:1158px"><svg width="14" height="26" viewBox="0 0 14 26"><path d="m2 2 10 11L2 24" stroke="#fff" stroke-width="2" fill="none"/></svg></div>
  <div class="abs dots"><span class="on"></span><span></span><span></span><span></span></div>
  <div class="abs quote-bar"></div>
</section>
<div class="abs quote-label">Quick Quote :</div>
<div class="abs q-input" style="left:379px;width:188px">Ship from...</div>
<div class="abs q-input" style="left:577px;width:187px">Ship to...</div>
<div class="abs q-go">GO</div>

<h2 class="abs h2" style="left:92px;top:722px">Why Choose us</h2>
<p class="abs para" style="left:92px;top:797px;width:480px">Lorem Ipsum is simply dummy text of the printing and typesetting industry. Lorem Ipsum has been the industry's standard dummy text ever.</p>
<div class="abs feature" style="left:92px;top:879px">
  <span class="ic"><svg width="26" height="26" viewBox="0 0 24 24"><path fill="#22b5a8" d="M3 4h2l3 10h9l2-7H7.5l-.6-2H21l-3 11H6.5L3.6 6H3zM9 19a1.5 1.5 0 1 1 0 .1zm7 0a1.5 1.5 0 1 1 0 .1z"/></svg></span>Logistic Services
</div>
<div class="abs dash" style="top:945px"></div>
<div class="abs feature" style="left:92px;top:958px">
  <span class="ic"><svg width="28" height="22" viewBox="0 0 28 22"><path fill="#22b5a8" d="M2 3h15v12H2zm16 4h5l3 4v4h-8zM6 16a2.5 2.5 0 1 1 0 .1zm15 0a2.5 2.5 0 1 1 0 .1z"/></svg></span>We are Really Fast
</div>
<div class="abs dash" style="top:1024px"></div>
<div class="abs feature" style="left:92px;top:1039px">
  <span class="ic"><svg width="26" height="26" viewBox="0 0 24 24"><path d="M4 14v-2a8 8 0 0 1 16 0v2" stroke="#22b5a8" stroke-width="2" fill="none"/><rect x="3" y="13" width="4" height="6" rx="1" fill="#22b5a8"/><rect x="17" y="13" width="4" height="6" rx="1" fill="#22b5a8"/></svg></span>24X7 Customer Support
</div>

<h2 class="abs h2" style="left:612px;top:722px">How it works</h2>
<p class="abs para" style="left:612px;top:797px;width:494px">Lorem Ipsum is simply dummy text of the printing and typesetting industry. It has been the industry's standard dummy text ever.</p>
<div class="abs video" role="img" aria-label="Video preview showing a white semi-truck driving through golden fields">
  <svg class="abs" style="left:208px;top:83px" width="78" height="62" viewBox="0 0 78 62"><circle cx="39" cy="31" r="30" fill="#e02a2a"/><path d="M31 18v26l22-13z" fill="#fff"/></svg>
</div>

<div class="abs deliver-photo" role="img" aria-label="Photo of a yellow truck hauling a white trailer on an open highway with mountains behind"></div>
<section class="abs deliver"></section>
<h2 class="abs h2" style="left:639px;top:1260px;color:#fff">What We can Deliver?</h2>
<p class="abs para" style="left:639px;top:1336px;width:500px;color:#fff">Lorem Ipsum is simply dummy text of the printing and typesetting industry. Lorem Ipsum has been the industry's standard dummy text ever</p>
<div class="abs cat" style="left:639px;top:1410px">
  <span class="ic"><svg width="26" height="22" viewBox="0 0 26 22"><rect x="2" y="5" width="22" height="14" rx="2" stroke="#fff" stroke-width="2" fill="none"/><path d="M9 1l4 4 4-4" stroke="#fff" stroke-width="2" fill="none"/></svg></span>Electronics
</div>
<div class="abs cat" style="left:813px;top:1408px">
  <span class="ic"><svg width="26" height="24" viewBox="0 0 26 24"><path d="M8 2 2 6l2 5 3-1v12h12V10l3 1 2-5-6-4c-1 2-3 3-5 3S9 4 8 2z" fill="#fff"/></svg></span>Clothings
</div>
<div class="abs cat" style="left:978px;top:1410px">
  <span class="ic"><svg width="22" height="26" viewBox="0 0 22 26"><path d="M3 2h12l4 4v18H3z" stroke="#fff" stroke-width="2" fill="none"/><path d="M7 11h8M7 15h8M7 19h6" stroke="#fff" stroke-width="2"/></svg></span>Documents
</div>
<a class="abs btn-view">VIEW ALL</a>

<section class="abs cream"></section>
<h2 class="abs h2" style="left:92px;top:1723px">Our Locations</h2>
<p class="abs para" style="left:92px;top:1797px;width:490px">Lorem Ipsum is simply dummy text of the printing and typesetting industry. Dummy texthas been the industry's standard dummy.</p>
<div class="abs map-card" style="left:92px">
  <div class="label">USA</div>
  <div class="map-shape" style="background:#2a7fd6" role="img" aria-label="Map of the United States with orange location pins"></div>
</div>
<div class="abs map-card" style="left:344px">
  <div class="label">CANADA</div>
  <div class="map-shape" style="background:#27b5a0" role="img" aria-label="Map of Canada with orange location pins"></div>
</div>

<h2 class="abs h2" style="left:699px;top:1723px">What Clients Say</h2>
<p class="abs quote-text">Lorem Ipsum is simply dummy text of printing and typesetting industry. Lorem Ipsum has been the industry's standard dummy text ever since 1500s, when unknown. Lorem Ipsum is simply dummy text of printing an typeseting industry. Lorem Ipsum has been the industry's it standard dummy. Lorem Ipsum has been industry's standard dummy text ever since 1500s</p>
<div class="abs client-name">Daniel Mercer,</div>
<div class="abs client-co">Northway Trading Co.</div>
<div class="abs nav-btn" style="left:1022px"><svg width="10" height="14" viewBox="0 0 10 14"><path d="M8 1 2 7l6 6" stroke="#fff" stroke-width="2.5" fill="none"/></svg></div>
<div class="abs nav-btn" style="left:1067px"><svg width="10" height="14" viewBox="0 0 10 14"><path d="m2 1 6 6-6 6" stroke="#fff" stroke-width="2.5" fill="none"/></svg></div>

<div class="abs clients-h"><h2 class="h2">Our Clients</h2></div>
<div class="abs client-box" style="left:56px" aria-label="Client logo placeholder"></div>
<div class="abs client-box" style="left:287px" aria-label="Client logo placeholder"></div>
<div class="abs client-box" style="left:520px" aria-label="Client logo placeholder"></div>
<div class="abs client-box" style="left:751px" aria-label="Client logo placeholder"></div>
<div class="abs client-box" style="left:984px" aria-label="Client logo placeholder"></div>

<footer class="abs footer"></footer>
<h3 class="abs f-h" style="left:92px">About us</h3>
<p class="abs f-text" style="left:92px;width:290px">Lorem Ipsum is simply dummy text of printing and typesetting industry. Lorem Ipsum has been the industry's standard dummy text ever since 1500s, when unknown. Lorem Ipsum is simply dummy text and of printing an typeseting industry. Lorem Ipsum has been the industry's standard.</p>
<h3 class="abs f-h" style="left:473px">Useful Links</h3>
<ul class="abs f-list" style="left:473px"><li>Home</li><li>About us</li><li>Services</li><li>Locations</li><li>News</li><li>Contact</li></ul>
<h3 class="abs f-h" style="left:680px">Help &amp; Support</h3>
<ul class="abs f-list" style="left:680px"><li>Help</li><li>Support</li><li>My bookings</li><li>Become a member</li><li>Terms &amp; conditions</li><li>Privacy Policy</li></ul>
<h3 class="abs f-h" style="left:892px">Contact us</h3>
<div class="abs f-contact" style="left:892px;top:2540px">
  <svg width="10" height="14" viewBox="0 0 10 14" style="margin-top:4px"><path d="M5 0a5 5 0 0 1 5 5c0 4-5 9-5 9S0 9 0 5a5 5 0 0 1 5-5z" fill="#f5a000"/></svg>
  <span>SwiftCargo, 48 Harbor Lane,<br>Newyork, USA, 10012</span>
</div>
<div class="abs f-contact" style="left:892px;top:2595px">
  <svg width="11" height="11" viewBox="0 0 24 24" style="margin-top:5px"><path fill="#f5a000" d="M6.6 10.8a15 15 0 0 0 6.6 6.6l2.2-2.2c.3-.3.7-.4 1-.2 1.1.4 2.3.6 3.6.6.6 0 1 .4 1 1V20c0 .6-.4 1-1 1A17 17 0 0 1 3 4c0-.6.4-1 1-1h3.5c.6 0 1 .4 1 1 0 1.3.2 2.5.6 3.6.1.3 0 .7-.2 1z"/></svg>
  <span>0155 010 2040, 0155 010 2041</span>
</div>
<div class="abs social" style="left:892px;top:2636px"><span></span><span></span><span></span><span></span></div>
<div class="abs footer-rule"></div>
<div class="abs brand" style="left:94px;top:2746px;color:#fff"><span class="dot"></span>SwiftCargo</div>
<div class="abs copy">©2016 SwiftCargo. All rights reserved</div>
<a class="abs btn-quote" style="left:986px;top:2740px;width:120px;height:47px">QUICK QUOTE</a>

</body>
</html>
```